WordPress website in children books redesign

We are personalised children storybook creators with a range of personalized books, music CDs and DVDs that are created for each child. We sell our concept through a license via distributors / entrepreneurs mainly based in France and Europe. We want to focus on selling B2C to parents and grandparents, looking to buy presents to their children aged 0 to 10 years old. Those present are educative, unique for each child, and they will learn to have fun and learn to have fun. I would like to redesign our WordPress website https://brightpebbletales.co.uk/index.php We are a children in the world of books and music books: books, music CDs and DVDs looking for something a little more along the lines of our competitors. See ike www.glimmerpage.com, www.tovikoro.com, www.lefiletdesetoiles.com, https://www.lespetitsvergers.com/, https://plumquestkids.com/ Our current website is a bit too old fashioned so I am looking at a much more modern design Here is a link for a few products that are not available here: https://www.filecrate.example/sh/kq417ptobnrelwx/ZZQ4rTfLmN8y-aBcDeFgHiJ-kl?dl=0 We have 2 sides in our website: B2C on the left side and B2B on the right site; B2B is for distributors that are entrepreneurs buying our concept. for the homepage design, the main focus will be B2Consumer Our current page is too blended, lacks reassurance elements and I would like to have a look at this page. from our current stories. here is a link for our business book to give you a feel for it: http://online.pagewhirl.example/qtpd/mnvs/ MAIN PAGES TO REVIEW / HOMEPAGE / https://brightpebbletales.co.uk/ BOOKS: https : //brightpebbletales.co.uk/product-category/personalised-books/ MUSIC: https://brightpebbletales.co.uk/product-category/music-cds/ BLOG: https://brightpebbletales.co.uk/blog -2 / Looking forward to seeing you and your questions asap

Target Market(s)

parents and grandparents of children aged 0 to 10 years old. This is for the European market

Industry/Entity Type

Publishing Company

Number of Pages Required

4 page

Colors
0392cd
9bcb3b
ec1f27
757575

Requirements
Must have
• keep within the color code of our RGB logo: D25028 RGB: 8CC364 329BC8 808285
Nice to have
• be more with the style of our competitors. Bright Pebble Tales am about making children learn the fun way, and develop their morality, self-esteem and confidence. It's about the magic of reading to help children learn while having fun. I have attached visuals but those are just examples and you we encourage you to suggest other ideas

```html
<!DOCTYPE html>
<html lang="en">
<head>
<meta charset="utf-8">
<title>Bright Pebble Tales – Home</title>
<link href="https://fonts.googleapis.com/css2?family=Noto+Serif:ital,wght@0,400;0,700;1,400&display=swap" rel="stylesheet">
<style>
:root{
  --cream:#ebe7da;
  --orange:#d25028;
  --green:#8cc364;
  --blue:#329bc8;
  --grey:#808285;
  --ink:#2b2b2b;
  --footer:#2e2e2e;
  --footer-text:#9b9b9b;
}
*{margin:0;padding:0;box-sizing:border-box}
html,body{width:1200px;height:1200px;overflow:hidden;background:#fff}
body{font-family:"Noto Serif",Georgia,serif;color:var(--ink)}
.page{position:absolute;left:289px;top:0;width:622px;height:1200px;background:var(--cream);overflow:hidden}
.abs{position:absolute}

/* header */
.nav-line{left:0;top:24px;width:622px;height:1px;background:#cfcabb}
.nav{top:8px;left:301px;display:flex;gap:0;font-size:6.5px;color:#333}
.nav span{position:absolute;white-space:nowrap}
.brand{left:77px;top:14px;width:60px;height:60px;border-radius:50%;background:#fff;display:flex;align-items:center;justify-content:center;text-align:center;font-size:8px;font-weight:700;color:var(--orange);line-height:1.15;box-shadow:0 0 0 2px #e3dfd2}

/* hero */
.hero-photo{left:285px;top:24px;width:260px;height:244px;background:linear-gradient(160deg,#f2d9b8 0%,#3b6ec0 45%,#c73a2a 70%,#1d2a3a 100%);opacity:.9}
.headline{left:78px;top:102px;font-style:italic;font-size:17px;line-height:20px;letter-spacing:.6px;color:#222}
.headline b{color:var(--orange);font-weight:700}
.cta{left:78px;top:194px}
.cta span{position:absolute;left:0;top:0;width:103px;height:24px;line-height:24px;text-align:center;color:#fff;font-size:8px}
.dots{top:268px;left:0;width:622px}

/* category cards */
.card{top:298px;width:147px;height:116px}
.card .title{position:absolute;left:17px;font-size:13.5px;font-weight:700;color:#fff;line-height:17px}

/* vision */
.vision-title{left:78px;top:460px;font-size:15px;letter-spacing:.3px}
.copy{font-size:7.2px;line-height:11.3px;color:#333}
.vision-copy{left:78px;top:486px;width:250px}
.vision-copy p{margin-bottom:11px}
.kids-panel{left:438px;top:444px;width:184px;height:146px;background:linear-gradient(135deg,#e4703a,#e8763e)}
.girl-photo{left:358px;top:464px;width:124px;height:134px;border:2px solid #fff;background:linear-gradient(150deg,#b9bdc6 0%,#dcd6d8 45%,#e8b7c9 75%,#c9a6b8 100%);box-shadow:0 1px 3px rgba(0,0,0,.15)}

/* video */
.video-card{left:77px;top:657px;width:268px;height:195px;background:#f4f2ec;border-radius:3px;box-shadow:0 2px 8px rgba(0,0,0,.18);z-index:2}
.video{position:absolute;left:13px;top:13px;width:242px;height:169px;background:linear-gradient(120deg,#8d8d8a 0%,#e9ddc9 35%,#f2ebe0 60%,#d8c48d 100%)}
.video-title{position:absolute;left:6px;top:8px;font-family:Arial,sans-serif;font-size:6.5px;color:#fff}
.learn-title{left:378px;top:670px;width:180px;font-size:12px;font-weight:700;line-height:14.5px;letter-spacing:.4px}
.learn-copy{left:378px;top:726px;width:162px}

/* blue band */
.band{left:0;top:824px;width:622px;height:225px;background:var(--blue)}
.band-stripe-g{left:0;top:824px;width:11px;height:225px;background:var(--green)}
.band-stripe-o{left:11px;top:824px;width:11px;height:225px;background:var(--orange)}
.band-copy{left:100px;top:872px;width:440px;font-size:8.3px;line-height:11.7px;color:#fff}
.band-copy p{margin-bottom:6px}

/* footer */
.footer{left:0;top:1049px;width:622px;height:151px;background:var(--footer)}
.col{top:1067px;font-size:7.6px}
.col h4{font-size:9.5px;font-weight:700;margin-bottom:6px;letter-spacing:.2px}
.col li{list-style:none;color:var(--footer-text);line-height:14.4px}
.col li::before{content:"›";margin-right:4px}
.col.c1 h4{color:var(--green)} .col.c1 li::before{color:var(--green)}
.col.c2 h4{color:var(--orange)} .col.c2 li::before{color:var(--orange)}
.col.c3 h4{color:var(--blue)} .col.c3 li::before{color:var(--blue)}
.col.c4 h4{color:#fff}
.social li::before{content:none}
.social li{display:flex;align-items:center;gap:8px;line-height:27px}
.social i{width:15px;height:15px;border-radius:50%;background:#1c1c1c;display:inline-block}
.foot-rule{left:78px;top:1168px;width:466px;height:1px;background:#444}
.legal{left:360px;top:1178px;width:186px;text-align:right;font-size:5.8px;color:#7a7a7a}
</style>
</head>
<body>
<div class="page">

  <!-- header -->
  <div class="abs nav-line"></div>
  <div class="abs nav" style="left:0;top:8px">
    <span style="left:301px">Our Products</span>
    <span style="left:358px">About Us</span>
    <span style="left:403px">Distributors</span>
    <span style="left:457px">Blog</span>
    <span style="left:486px">Contact</span>
  </div>
  <svg class="abs" style="left:528px;top:5px" width="16" height="14" viewBox="0 0 16 14" aria-label="Cart">
    <path d="M1 2h3l2 7h7l2-5H5" fill="none" stroke="#6aa84f" stroke-width="1.4"/>
    <circle cx="7" cy="12" r="1.2" fill="#6aa84f"/><circle cx="12" cy="12" r="1.2" fill="#6aa84f"/>
  </svg>
  <div class="abs brand">Bright<br>Pebble<br>Tales</div>

  <!-- hero -->
  <div class="abs hero-photo" role="img" aria-label="Child in a superhero mask and cape holding a personalised Super-heroes storybook"></div>
  <div class="abs headline">When children become<br>the <b>heroes</b> of their<br>own stories</div>
  <div class="abs cta">
    <svg width="103" height="24" viewBox="0 0 103 24"><path d="M0 0H103L97 12L103 24H0L6 12Z" fill="var(--orange)"/></svg>
    <span>Create your Book</span>
  </div>
  <svg class="abs" style="left:0;top:244px" width="622" height="36" viewBox="0 0 622 36">
    <path d="M0 32L331 6L622 32V36H0Z" fill="var(--cream)"/>
    <path d="M0 28L331 2L622 28" fill="none" stroke="var(--blue)" stroke-width="2"/>
    <path d="M0 30.5L331 4.5L622 30.5" fill="none" stroke="var(--orange)" stroke-width="2"/>
    <path d="M0 33L331 7L622 33" fill="none" stroke="var(--green)" stroke-width="1.6"/>
  </svg>
  <svg class="abs dots" height="8" viewBox="0 0 622 8">
    <circle cx="298" cy="4" r="2.2" fill="#9cc8dd"/>
    <circle cx="312" cy="4" r="3.2" fill="none" stroke="var(--blue)" stroke-width="1"/>
    <circle cx="312" cy="4" r="1.8" fill="var(--blue)"/>
    <circle cx="325" cy="4" r="2.2" fill="#9cc8dd"/>
  </svg>

  <!-- category cards -->
  <div class="abs card" style="left:78px">
    <svg width="147" height="116" viewBox="0 0 147 116"><path d="M0 0H147V116L73.5 104L0 116Z" fill="#d9592f"/>
      <g fill="none" stroke="#222" stroke-width="1.5"><circle cx="36" cy="22" r="5"/><path d="M20 36l16 5 16-5v15l-16 5-16-5Z"/><path d="M36 41v15"/></g>
    </svg>
    <div class="title" style="top:62px">Personalised<br>Books</div>
  </div>
  <div class="abs card" style="left:237px">
    <svg width="147" height="116" viewBox="0 0 147 116"><path d="M0 0H147V116L73.5 104L0 116Z" fill="#84c56a"/>
      <g fill="none" stroke="#222" stroke-width="1.5"><path d="M24 38a15 15 0 0 1 30 0"/><rect x="20" y="36" width="6" height="11" rx="2"/><rect x="52" y="36" width="6" height="11" rx="2"/></g>
    </svg>
    <div class="title" style="top:62px">Music</div>
  </div>
  <div class="abs card" style="left:396px">
    <svg width="147" height="116" viewBox="0 0 147 116"><path d="M0 0H147V116L73.5 104L0 116Z" fill="#329bc8"/>
      <g fill="none" stroke="#222" stroke-width="1.5"><circle cx="35" cy="30" r="12"/><circle cx="35" cy="30" r="3"/><circle cx="46" cy="40" r="6" fill="#329bc8"/></g>
    </svg>
    <div class="title" style="top:62px">DVD Cartoon</div>
  </div>

  <!-- vision -->
  <div class="abs vision-title">Our Vision</div>
  <div class="abs copy vision-copy">
    <p>Is to make children the heroes of the adventure and live magical and unforgettable moments they can share with their family and friends.</p>
    <p>Scenarios are adapted to every age, imagined and conceived in association with children, schools, speech therapists, psychologists and childhood experts.</p>
  </div>
  <div class="abs kids-panel" role="img" aria-label="Orange panel with hand-drawn kids doodles"></div>
  <div class="abs girl-photo" role="img" aria-label="Little girl in a princess crown holding a personalised book"></div>

  <!-- video -->
  <div class="abs band-stripe-g"></div>
  <div class="abs band-stripe-o"></div>
  <div class="abs band"></div>
  <div class="abs video-card">
    <div class="video" role="img" aria-label="Video still of two girls reading a personalised book together">
      <div class="video-title">Livres personnalisés Petits Galets / Personalised books</div>
      <svg style="position:absolute;left:112px;top:76px" width="28" height="19" viewBox="0 0 28 19">
        <rect width="28" height="19" rx="5" fill="#222" opacity=".85"/><path d="M11 5l8 4.5-8 4.5Z" fill="#fff"/>
      </svg>
    </div>
  </div>
  <div class="abs learn-title">Personalisation improves a child’s learning ability &amp; motivation</div>
  <div class="abs copy learn-copy">Bright Pebble Tales personalised books offers the possibility of sharing magical and unique moments which help the child become familiar with reading and inspire reading passion. Which is more special and magical than becoming the hero of your own story!</div>

  <div class="abs band-copy">
    <p>Bright Pebble Tales has created and developed a unique concept that allows you to prepare and sell high quality award–winning personalised children books in few minutes only.</p>
    <p>In each story, the children become the heroes of the adventure and lives magical and unforgettable moments they can share with their family and friends.</p>
    <p>Our products aim to stimulate learning and enhance reading passion from an early age. They have been designed with high-quality original artwork with bright colours to fully engage a child’s imagination. Personalisation offers children the opportunity to recognise themselves in the story, thus developing self-esteem and confidence. The stories are written in an educational and informative way, whilst remaining fun, positive, and engaging.</p>
    <p>Scenarios are adapted to every age, imagined and conceived in association with children, schools, speech therapists, psychologists and childhood experts.</p>
  </div>

  <!-- footer -->
  <div class="abs footer"></div>
  <div class="abs col c1" style="left:78px"><h4>Our Collections</h4><ul><li>Personalised books</li><li>Personalised music albums</li><li>Personalised DVD cartoon</li><li>Personalised school books</li></ul></div>
  <div class="abs col c2" style="left:225px"><h4>Discovery Pack</h4><ul><li>Gold pack</li><li>Platinium pack</li><li>Success stories</li></ul></div>
  <div class="abs col c3" style="left:332px"><h4>Order Samples</h4><ul><li>About Us</li><li>Contact Us</li><li>Recruitment</li></ul></div>
  <div class="abs col c4 social" style="left:438px"><h4>Be a part of Bright Pebble Tales</h4><ul style="margin-top:-4px"><li><i></i>Chatterbook</li><li><i></i>Snapframe</li><li><i></i>Pinlattice</li></ul></div>
  <div class="abs foot-rule"></div>
  <svg class="abs" style="left:98px;top:1179px" width="30" height="8" viewBox="0 0 30 8" aria-label="Language: French, English">
    <rect x="0" y="0" width="3.7" height="7" fill="#2c4fa3"/><rect x="3.7" y="0" width="3.6" height="7" fill="#fff"/><rect x="7.3" y="0" width="3.7" height="7" fill="#d22"/>
    <rect x="18" y="0" width="11" height="7" fill="#fff"/>
    <g fill="#c33"><rect x="18" y="0" width="11" height="1"/><rect x="18" y="2" width="11" height="1"/><rect x="18" y="4" width="11" height="1"/><rect x="18" y="6" width="11" height="1"/></g>
    <rect x="18" y="0" width="5" height="4" fill="#2c4fa3"/>
  </svg>
  <div class="abs legal">© 2018 Bright Pebble Tales All rights reserved. &nbsp;&nbsp; Terms and conditions</div>
</div>
</body>
</html>
```